Events Company Needs Website Revamp

Corvid Expos is an events company that specializes in organizing and marketing large scale consumer and trade events globally.

The new web design should provide easy classification of the events, and allow visitors to find and access the details page within 2 clicks.

There are no strict guidelines on the color theme. It just has to blend naturally with the corporate logo.

The company logo is uploaded (pdf & ai)

I came across this design which I like very much. Elegant and corporate with nice modern fonttype.

Layout wise, neat and clear. 

Please see how you can emulate the design further. Particularly, highlighting the 2 event arms (Trade/Consumer) clearly.

Target Market(s)

Consumer looking for upcoming events, B2C companies looking to participate, B2B companies looking to connect with other companies

Industry/Entity Type

It Company

Requirements
Must have
• The new design should help to achieve the following objectives:
1) Visitors should be able to easily identify and access the 2 different types of events (i.e. Trade Events and Consumer Events).
2) Visitors should be able to easily find events that interest them (e.g. filter by date, trade or consumer, category [i.e. beauty, retail, F&B, construction, etc.]).
3) Visitors should be able to access an event’s details page within 2 clicks from any page.

Main navigation to include the following links:
- About Us
- Calendar
- Consumer Events
- Trade Events
- Contact Us

Design for Three (3) pages required:
A. Homepage
- Clear differentiation and easy access to the 2 different types of events (trade and consumer)
- Featured area to showcase latest 4-5 events
- Quick way to access events calendar
- Clear call-to-action for newsletter signup
- Social media sharing widgets/buttons
- A section for latest news and press releases
- A section for featured testimonials

B. Events Listing Page
- List of links to all events
- Logos and/or photos of events
- Filter / tags to find events in a specific category (e.g. food, electronics, building & construction, etc.)

C. Events Details Page
- Photo strip to showcase event photos / brochure
- A section with event details (Date, Venue, Event Description, etc.)
- Call-to-action button to visit event website
- Call-to-action button to contact event sales team
- E.g. http://plimva.net/user/drenholt/lantern-fairweek-2011 but with the photo strip permanently extended and of a shorter height. Event details and call-to-action buttons should also be easily seen

```html
<!DOCTYPE html>
<html lang="en">
<head>
<meta charset="utf-8">
<title>Corvid Expos — Home</title>
<link rel="stylesheet" href="https://fonts.googleapis.com/css2?family=Gelasio:ital@0;1&family=Open+Sans:wght@400;600;700&family=Exo+2:wght@600&display=swap">
<style>
:root{
  --orange:#f0812d;
  --orange-dark:#d9661a;
  --red:#c8321c;
  --black:#111;
  --charcoal:#454545;
  --grey-bg:#e9e9e9;
  --panel:#f3f3f3;
  --line:#d8d8d8;
  --text:#444;
  --muted:#999;
  --white:#fff;
  --pink:#d43a9c;
  --blue:#2f7fd0;
  --gold:#e0a41f;
  --fuchsia:#c63fd0;
}
*{margin:0;padding:0;box-sizing:border-box}
html,body{width:1000px;height:1200px;overflow:hidden}
body{background:var(--grey-bg);font-family:"Open Sans",sans-serif;color:var(--text);position:relative}
.abs{position:absolute}
.outer-panel{left:92px;top:0;width:816px;height:1200px;background:#f4f4f4}
.page{left:166px;top:0;width:668px;height:1010px;background:var(--white)}
.phone-tab{left:697px;top:0;width:141px;height:28px;background:linear-gradient(#fbb35a,var(--orange));color:var(--red);font-size:15px;font-weight:600;display:flex;align-items:center;gap:8px;padding-left:12px}
.phone-tab svg{width:12px;height:12px}
.main-nav{left:174px;top:56px;width:652px;height:22px;background:var(--black);display:flex;padding-left:150px}
.main-nav a{color:var(--white);font-size:9.5px;text-decoration:none;display:flex;align-items:center;padding:0 16px;border-right:1px solid #333;text-transform:uppercase}
.main-nav a.active{background:var(--orange)}
.logo-box{left:187px;top:10px;width:125px;height:96px;background:var(--white);box-shadow:0 1px 4px rgba(0,0,0,.25);display:flex;flex-direction:column;align-items:center;justify-content:center;gap:6px;z-index:2}
.logo-name{display:flex;align-items:center;gap:6px;color:var(--orange-dark);font-size:15px;font-weight:700}
.logo-name .dot{width:14px;height:14px;border-radius:50%;background:var(--orange)}
.logo-sub{font-size:7px;color:#1c5fa8;letter-spacing:.3px}
.hero-frame{left:174px;top:78px;width:652px;height:274px;background:var(--orange)}
.hero-photo{left:181px;top:86px;width:638px;height:259px;background:linear-gradient(90deg,#6f7a86,#c9cfd6 40%,#a7b0ba 70%,#8a8177)}
.arrow{top:200px;width:30px;height:30px;background:var(--white);box-shadow:0 1px 3px rgba(0,0,0,.3);display:flex;align-items:center;justify-content:center}
.arrow svg{width:20px;height:20px}
.finder{left:174px;top:357px;width:652px;height:81px;background:var(--charcoal)}
.finder-corner{left:174px;top:357px}
.finder h2{left:207px;top:366px;font-family:"Exo 2",sans-serif;font-size:17px;color:var(--white);font-weight:600}
.select{top:397px;width:117px;height:23px;border-radius:3px;background:linear-gradient(#f6f6f6,#d8d8d8);font-size:8.5px;color:#777;padding:0 8px;display:flex;align-items:center;justify-content:space-between}
.select i{border:5px solid transparent;border-top:6px solid #444;margin-top:5px}
.filter-btn{left:748px;top:396px;width:62px;height:23px;border-radius:3px;background:linear-gradient(#ff6a45,#d72d12);color:var(--white);font-family:"Exo 2",sans-serif;font-size:11px;display:flex;align-items:center;justify-content:center;gap:4px}
.card{top:452px;width:146px}
.card .tag{position:absolute;left:0;top:0;height:15px;padding:0 6px;font-family:Gelasio,serif;font-size:9px;color:var(--white);text-transform:uppercase;line-height:15px;z-index:1}
.card .thumb{position:absolute;left:6px;top:8px;width:140px;height:70px;clip-path:polygon(0 0,100% 0,100% 80%,88% 100%,0 100%)}
.card p{position:absolute;left:6px;top:84px;width:136px;font-size:8.3px;line-height:11px;color:#555}
.card .more{position:absolute;left:6px;top:128px;font-size:8px;color:#555}
.feature{left:174px;width:449px;height:95px;border:1px solid var(--line)}
.feature .ring{position:absolute;left:12px;top:-2px;width:100px;height:100px;border-radius:50%;background:var(--white);box-shadow:0 0 4px rgba(0,0,0,.2)}
.feature .photo{position:absolute;left:5px;top:5px;width:90px;height:90px;border-radius:50%}
.feature h3{position:absolute;left:122px;top:-12px;background:var(--white);padding:0 6px;font-family:Gelasio,serif;font-weight:400;font-size:18px;color:#222}
.feature h3 em,.section-title em{color:var(--orange)}
.feature p{position:absolute;left:123px;top:14px;width:310px;font-size:8.4px;line-height:12.4px}
.feature .more{position:absolute;right:10px;bottom:8px;font-size:8px}
.calendar-box{left:643px;top:627px;width:183px;height:205px;border:1px solid var(--line);background:#f7f7f7}
.calendar-title{left:692px;top:617px;padding:0 6px;background:var(--white);font-family:Gelasio,serif;font-size:17px;color:#222}
.cal-head{left:650px;top:658px;width:169px;height:25px;background:var(--red);color:var(--white);font-size:10px;letter-spacing:1px;display:flex;align-items:center;justify-content:space-between;padding:0 8px}
.cal-grid{left:650px;top:683px;width:169px;display:grid;grid-template-columns:repeat(7,1fr)}
.cal-grid span{height:24px;border-right:1px solid #ddd;border-bottom:1px solid #ddd;background:var(--white);font-size:11px;display:flex;align-items:center;justify-content:center;color:#222}
.cal-grid span.dow{height:20px;font-size:7px;color:#888;background:#f4f4f4}
.cal-grid span.today{background:var(--red);color:var(--white)}
.cal-grid span.past{background:#ddd;color:#888}
.section-title{font-family:Gelasio,serif;font-size:17px;color:#222;font-weight:400}
.panel{background:var(--panel)}
.dots{left:460px;top:856px;display:flex;gap:4px}
.dots i{width:5px;height:5px;border-radius:50%;background:#ccc}
.dots i:first-child{background:#666}
.mini-photo{background:linear-gradient(135deg,#d9c5b5,#a8b8c9)}
.footer{left:160px;top:1003px;width:680px;height:197px;background:radial-gradient(ellipse at 45% 20%,#6a6a6a,#3a3a3a 55%,#333)}
.footer-strip{left:160px;top:1003px;width:680px;height:40px;background:rgba(0,0,0,.35)}
.newsletter{left:180px;top:1029px;width:202px;height:95px;background:var(--orange);padding:10px 12px}
.newsletter h4{font-size:8px;color:var(--black);font-weight:700}
.newsletter p{font-size:8.8px;color:var(--white);line-height:12px;margin-top:4px}
.email{left:190px;top:1090px;width:140px;height:18px;background:var(--white);font-size:8.5px;color:#888;padding-left:6px;line-height:18px}
.submit{left:330px;top:1090px;width:55px;height:18px;background:#2a5f8b;color:var(--white);font-size:9px;font-weight:700;line-height:18px;text-align:center;clip-path:polygon(0 0,92% 0,100% 50%,92% 100%,0 100%)}
.foot-col h5{font-size:7.5px;color:var(--white);font-weight:700;margin-bottom:12px}
.foot-col a{display:block;font-size:8px;color:#b4b4b4;line-height:12.3px;text-decoration:none}
.foot-col p{font-size:8px;color:#ccc;font-weight:600;line-height:12.3px}
.social{display:flex;gap:6px}
.social i{width:22px;height:22px;border-radius:3px}
.copyright{left:0;top:1171px;width:1000px;text-align:center;font-size:8px;color:#aaa}
</style>
</head>
<body>
<div class="abs outer-panel"></div>
<div class="abs page"></div>

<div class="abs phone-tab">
  <svg viewBox="0 0 24 24"><path fill="#c8321c" d="M6.6 10.8a15 15 0 0 0 6.6 6.6l2.2-2.2c.3-.3.7-.4 1-.2 1.1.4 2.3.6 3.6.6.6 0 1 .4 1 1V20c0 .6-.4 1-1 1A17 17 0 0 1 3 4c0-.6.4-1 1-1h3.5c.6 0 1 .4 1 1 0 1.3.2 2.5.6 3.6.1.3 0 .7-.2 1z"/></svg>
  555 0134 2270
</div>

<nav class="abs main-nav">
  <a class="active" href="#">Home</a>
  <a href="#">About Us</a>
  <a href="#">Calendar</a>
  <a href="#">Consumer Events</a>
  <a href="#">Trade Events</a>
  <a href="#" style="border:none">Contact Us</a>
</nav>

<div class="abs logo-box">
  <div class="logo-name"><span class="dot"></span>Corvid Expos</div>
  <div class="logo-sub">A SUBSIDIARY OF HALDEN MEDIA</div>
</div>

<div class="abs hero-frame"></div>
<div class="abs hero-photo" role="img" aria-label="Business audience applauding at a conference"></div>
<div class="abs arrow" style="left:165px"><svg viewBox="0 0 20 20"><circle cx="10" cy="10" r="8.5" fill="none" stroke="#c8321c" stroke-width="2"/><path d="M11.5 6 7.5 10l4 4" fill="none" stroke="#c8321c" stroke-width="2"/></svg></div>
<div class="abs arrow" style="left:805px"><svg viewBox="0 0 20 20"><circle cx="10" cy="10" r="8.5" fill="none" stroke="#c8321c" stroke-width="2"/><path d="M8.5 6l4 4-4 4" fill="none" stroke="#c8321c" stroke-width="2"/></svg></div>

<div class="abs finder"></div>
<svg class="abs finder-corner" width="40" height="34" viewBox="0 0 40 34"><path d="M0 0h38L0 34z" fill="#f0812d"/><path d="M0 0h38L0 34z" fill="none"/></svg>
<h2 class="abs" style="left:207px;top:366px;font-family:'Exo 2',sans-serif;font-size:17px;color:#fff;font-weight:600">FIND EVENTS</h2>
<div class="abs select" style="left:206px">Date<i></i></div>
<div class="abs select" style="left:340px">Trade &amp; Consumer<i></i></div>
<div class="abs select" style="left:474px">Category<i></i></div>
<div class="abs select" style="left:608px">All Events<i></i></div>
<div class="abs filter-btn">FILTER <svg width="12" height="12" viewBox="0 0 12 12"><circle cx="5" cy="5" r="3.5" fill="none" stroke="#fff" stroke-width="1.5"/><path d="M7.5 7.5 11 11" stroke="#fff" stroke-width="1.8"/></svg></div>

<div class="abs card" style="left:174px">
  <span class="tag" style="background:var(--red)">Popular Events</span>
  <div class="thumb" role="img" aria-label="Model at a beauty showcase" style="background:linear-gradient(135deg,#5a2a6e,#b04a9c)"></div>
  <p>Lorem Ipsum is simply dummy text of the printing and typesetting industry dummy text...</p>
  <span class="more">Read More ▸</span>
</div>
<div class="abs card" style="left:341px">
  <span class="tag" style="background:var(--blue)">Culture Events</span>
  <div class="thumb" role="img" aria-label="Cultural performers on stage" style="background:linear-gradient(135deg,#2c4a7a,#c9c5c0 60%,#b8322b)"></div>
  <p>Lorem Ipsum is simply dummy text of the printing and typesetting industry dummy text...</p>
  <span class="more">Read More ▸</span>
</div>
<div class="abs card" style="left:510px">
  <span class="tag" style="background:var(--gold)">Musical Events</span>
  <div class="thumb" role="img" aria-label="Band performing live" style="background:linear-gradient(135deg,#233a5e,#6f86a8)"></div>
  <p>Lorem Ipsum is simply dummy text of the printing and typesetting industry dummy text...</p>
  <span class="more">Read More ▸</span>
</div>
<div class="abs card" style="left:680px">
  <span class="tag" style="background:var(--fuchsia)">Fashion Events</span>
  <div class="thumb" role="img" aria-label="Guests at a fashion party" style="background:linear-gradient(135deg,#3a2a24,#c9a78a)"></div>
  <p>Lorem Ipsum is simply dummy text of the printing and typesetting industry dummy text...</p>
  <span class="more">Read More ▸</span>
</div>

<section class="abs feature" style="top:623px">
  <div class="ring"><div class="photo" role="img" aria-label="Trade delegates at a seminar" style="background:linear-gradient(135deg,#e0d2c2,#8aa0b8)"></div></div>
  <h3>Trade <em>Events</em></h3>
  <p>Lorem Ipsum is simply dummy text of the printing and typesetting industry. Lorem Ipsum has been the industry's standard dummy text ever since the 1500s, when an unknown printer took a galley of type and scrambled it to make a type specimen booktially unchanged.</p>
  <span class="more">Read More ▸</span>
</section>
<section class="abs feature" style="top:738px">
  <div class="ring"><div class="photo" role="img" aria-label="Consumer audience seated at an event" style="background:linear-gradient(135deg,#3a4a6a,#b8a08a)"></div></div>
  <h3>Consumer <em>Events</em></h3>
  <p>Lorem Ipsum is simply dummy text of the printing and typesetting industry. Lorem Ipsum has been the industry's standard dummy text ever since the 1500s, when an unknown printer took a galley of type and scrambled it to make a type specimen booktially unchanged.</p>
  <span class="more">Read More ▸</span>
</section>

<div class="abs calendar-box"></div>
<div class="abs calendar-title">Calendar</div>
<div class="abs cal-head"><span>‹</span><span>MAY 2012</span><span>›</span></div>
<div class="abs cal-grid">
  <span class="dow">SUN</span><span class="dow">MON</span><span class="dow">TUE</span><span class="dow">WED</span><span class="dow">THU</span><span class="dow">FRI</span><span class="dow">SAT</span>
  <span></span><span>1</span><span>2</span><span>3</span><span>4</span><span>5</span><span>6</span>
  <span>7</span><span>8</span><span>9</span><span>10</span><span>11</span><span class="past">12</span><span>13</span>
  <span>14</span><span>15</span><span class="today">16</span><span>17</span><span>18</span><span>19</span><span>20</span>
  <span>21</span><span>22</span><span>23</span><span>24</span><span>25</span><span>26</span><span>27</span>
  <span>28</span><span>29</span><span>30</span><span>31</span><span></span><span></span><span></span>
</div>

<h3 class="abs section-title" style="left:187px;top:848px">Client <em>Testimonials</em></h3>
<div class="abs dots"><i></i><i></i><i></i></div>
<div class="abs panel" style="left:174px;top:870px;width:320px;height:114px"></div>
<svg class="abs" style="left:366px;top:984px" width="12" height="14"><path d="M0 0h12L6 14z" fill="#f3f3f3"/></svg>
<div class="abs mini-photo" role="img" aria-label="Client team portrait" style="left:187px;top:884px;width:64px;height:64px;border:3px solid #fff;box-shadow:0 1px 3px rgba(0,0,0,.25)"></div>
<p class="abs" style="left:266px;top:881px;width:215px;font-size:8.4px;line-height:12.4px">Lorem Ipsum is simply dummy text of the printing and typesetting industry. Lorem Ipsum has been the industry's standard dummy text 1500s, when an unknown printer took a galley of type and scrambled it to make a &nbsp;booktially unchanged.</p>
<span class="abs" style="left:396px;top:987px;font-size:9px;font-style:italic;color:#333">Dara Quill</span>

<h3 class="abs section-title" style="left:520px;top:848px">Latest News &amp; <em>Press Releases</em></h3>
<div class="abs panel" style="left:507px;top:870px;width:319px;height:114px"></div>
<div class="abs mini-photo" role="img" aria-label="News thumbnail" style="left:520px;top:884px;width:34px;height:34px"></div>
<span class="abs" style="left:568px;top:883px;font-size:7px;color:#888">16 March, 2012</span>
<p class="abs" style="left:568px;top:894px;width:250px;font-size:8.4px;line-height:12px">Lorem Ipsum is simply dummy text of the printing and type setting industry...</p>
<div class="abs mini-photo" role="img" aria-label="News thumbnail" style="left:520px;top:931px;width:34px;height:34px"></div>
<span class="abs" style="left:568px;top:931px;font-size:7px;color:#888">28 April, 2012</span>
<p class="abs" style="left:568px;top:942px;width:250px;font-size:8.4px;line-height:12px">Lorem Ipsum is simply dummy text of the printing and type setting industry...</p>
<span class="abs" style="left:761px;top:968px;font-size:8px">More News ▸</span>

<footer>
  <div class="abs footer"></div>
  <div class="abs footer-strip"></div>
  <div class="abs newsletter">
    <h4>NEWSLETTER</h4>
    <p>Lorem Ipsum is simply dummy text of the printing and typesetting industry.</p>
  </div>
  <div class="abs email">enter your e-mail address</div>
  <div class="abs submit">SUBMIT</div>

  <div class="abs foot-col" style="left:402px;top:1060px">
    <h5>CONNECT WITH US</h5>
    <div class="social" aria-label="Social links">
      <i style="background:#3b5b99"></i><i style="background:#3fb3e0"></i><i style="background:#1d76b3"></i><i style="background:#2d8ccf"></i>
    </div>
  </div>
  <div class="abs foot-col" style="left:556px;top:1060px">
    <h5>QUICK LINKS</h5>
    <a href="#">Home</a><a href="#">About us</a><a href="#">Calendar</a><a href="#">Trade Events</a><a href="#">Consumer Events</a>
  </div>
  <div class="abs foot-col" style="left:642px;top:1060px">
    <h5>EVENTS</h5>
    <a href="#">Popular Events</a><a href="#">Culture Events</a><a href="#">Musical Events</a><a href="#">Fashion Events</a><a href="#">Corporate Events</a>
  </div>
  <div class="abs foot-col" style="left:722px;top:1060px;width:100px">
    <h5>CONTACT US</h5>
    <p>Lorem Ipsum is simply dummy text of the printing and type setting industry.</p>
  </div>
  <div class="abs copyright">Copyright© 2012 Corvid Expos. All Right Reserved.</div>
</footer>
</body>
</html>
```